New business card design

I need original, modern, business looking but dzen (minimalistic) looking design.
Also refer to websit trevanix.ru

Text is

Дробышев Кирилл, PMP
Партнер

Моб. +7 (915) 460 7185
info@trevanix.ru
Москва, Россия, 117342, ул. Береговая 7/2
=====================

Drobyshev Kirill, PMP
Partner

Mob. +7 (915) 460 7185
info@trevanix.ru
Moscow, Russia,117342, Beregovaya 7/2

Industry/Entity Type

Business

Font styles to use
Serif
Sans Serif

```html
<!DOCTYPE html>
<html lang="ru">
<head>
<meta charset="utf-8">
<title>Trevanix — business cards</title>
<link rel="stylesheet" href="https://fonts.googleapis.com/css2?family=Didact+Gothic&display=swap">
<style>
  :root {
    --backdrop: #d6d6d6;
    --card: #ffffff;
    --ink: #1c1c1c;
    --accent: #1a86c8;
    --brand: #2a9fd8;
    --rule: #222222;
  }
  * { margin: 0; padding: 0; box-sizing: border-box; }
  html, body {
    width: 1200px; height: 424px; overflow: hidden;
    background: var(--backdrop);
    font-family: "Didact Gothic", "Century Gothic", sans-serif;
    color: var(--ink);
  }
  .card {
    position: absolute; top: 80px;
    width: 441px; height: 255px;
    background: var(--card);
  }
  .card--en { left: 104px; }
  .card--ru { left: 657px; }
  .brand {
    position: absolute; left: 26px; top: 92px;
    display: flex; align-items: center; gap: 10px;
  }
  .brand__mark {
    width: 32px; height: 32px; background: var(--brand);
  }
  .brand__name {
    font-size: 30px; color: var(--brand); letter-spacing: 0.2px;
  }
  .divider {
    position: absolute; left: 219px; top: 53px;
    width: 2px; height: 149px; background: var(--rule);
  }
  .details { position: absolute; left: 242px; top: 70px; }
  .card--ru .details { top: 73px; }
  .person__name { font-size: 15px; line-height: 17px; }
  .person__role { font-size: 13px; line-height: 15px; color: var(--accent); }
  .contacts { list-style: none; margin-top: 18px; }
  .contact {
    display: flex; align-items: flex-start; gap: 9px;
    font-size: 12px; line-height: 14px; margin-bottom: 11px;
  }
  .contact__icon { flex: none; width: 13px; height: 13px; }
</style>
</head>
<body>

<section class="card card--en" lang="en">
  <div class="brand"><span class="brand__mark"></span><span class="brand__name">Trevanix</span></div>
  <div class="divider"></div>
  <div class="details">
    <p class="person__name">Drobyshev Kirill, PMP</p>
    <p class="person__role">Partner</p>
    <ul class="contacts">
      <li class="contact">
        <svg class="contact__icon" viewBox="0 0 13 13"><rect width="13" height="13" fill="#1a86c8"/><rect x="4" y="2" width="5" height="9" rx="1" fill="none" stroke="#fff" stroke-width="1.2"/></svg>
        <span>+7 (915) 460 7185</span>
      </li>
      <li class="contact">
        <svg class="contact__icon" viewBox="0 0 13 13"><rect width="13" height="13" fill="#1a86c8"/><circle cx="5.5" cy="5.5" r="2.8" fill="none" stroke="#fff" stroke-width="1.3"/><line x1="7.6" y1="7.6" x2="10.5" y2="10.5" stroke="#fff" stroke-width="1.5"/></svg>
        <span>info@trevanix.ru</span>
      </li>
      <li class="contact">
        <svg class="contact__icon" viewBox="0 0 13 13"><rect width="13" height="13" fill="#1a86c8"/><path d="M6.5 11.5 L3.6 6.4 A3.3 3.3 0 1 1 9.4 6.4 Z" fill="#fff"/><circle cx="6.5" cy="4.9" r="1.2" fill="#1a86c8"/></svg>
        <span>Moscow, Russia<br>117342, Beregovaya 7/2</span>
      </li>
    </ul>
  </div>
</section>

<section class="card card--ru">
  <div class="brand"><span class="brand__mark"></span><span class="brand__name">Trevanix</span></div>
  <div class="divider"></div>
  <div class="details">
    <p class="person__name">Дробышев Кирилл, PMP</p>
    <p class="person__role">Партнер</p>
    <ul class="contacts">
      <li class="contact">
        <svg class="contact__icon" viewBox="0 0 13 13"><rect width="13" height="13" fill="#1a86c8"/><rect x="4" y="2" width="5" height="9" rx="1" fill="none" stroke="#fff" stroke-width="1.2"/></svg>
        <span>+7 (915) 460 7185</span>
      </li>
      <li class="contact">
        <svg class="contact__icon" viewBox="0 0 13 13"><rect width="13" height="13" fill="#1a86c8"/><circle cx="5.5" cy="5.5" r="2.8" fill="none" stroke="#fff" stroke-width="1.3"/><line x1="7.6" y1="7.6" x2="10.5" y2="10.5" stroke="#fff" stroke-width="1.5"/></svg>
        <span>info@trevanix.ru</span>
      </li>
      <li class="contact">
        <svg class="contact__icon" viewBox="0 0 13 13"><rect width="13" height="13" fill="#1a86c8"/><path d="M6.5 11.5 L3.6 6.4 A3.3 3.3 0 1 1 9.4 6.4 Z" fill="#fff"/><circle cx="6.5" cy="4.9" r="1.2" fill="#1a86c8"/></svg>
        <span>Москва, Россия<br>117342, ул. Береговая 7/2</span>
      </li>
    </ul>
  </div>
</section>

</body>
</html>
```